COMPANY SIGN

I am in the process of ordering new company For Sale signs and stationary (business cards, envelopes, letterheads, and labels). I need a new design with my existing company logo. The TWO MOST IMPORTANT PROJECTS I need right now is the new design for the company sign and business cards. I've uploaded a .jpg file of my company logo.

I like the design to be eye catching and the background color of the company sign to be soothing to the eyes. Perhaps, using one of the color on the leaves of the logo or any other color that the designer think will go well with the logo. My favorite colors are teal or light olive color but don't let that affect your creativity.

Industry/Entity Type

Business

Requirements
Should not have
• Please don't use "Times New Roman" fonts or fonts that is hard to read.

```html
<!DOCTYPE html>
<html lang="en">
<head>
<meta charset="utf-8">
<title>Maplewood Home Tour – Company Sign</title>
<link rel="stylesheet" href="https://fonts.googleapis.com/css2?family=Marcellus&display=swap">
<style>
  :root {
    --olive: #b7bc80;
    --lime: #b3c744;
    --bark: #5a4530;
    --cream: #c9cb8f;
    --edge: #8a8a7a;
    --page: #ffffff;
  }
  html, body {
    margin: 0;
    padding: 0;
    width: 1200px;
    height: 1194px;
    overflow: hidden;
    background: var(--page);
  }
  .sign {
    position: relative;
    box-sizing: border-box;
    width: 1200px;
    height: 1194px;
    border: 2px solid var(--edge);
    border-radius: 30px;
    overflow: hidden;
    background: var(--olive);
    font-family: "Marcellus", "Optima", sans-serif;
  }
  .brand {
    position: absolute;
    left: 0;
    top: 0;
    width: 100%;
    height: 736px;
    display: flex;
    flex-direction: column;
    align-items: center;
    justify-content: center;
    gap: 44px;
    padding-top: 60px;
    box-sizing: border-box;
  }
  .brand-mark {
    width: 150px;
    height: 150px;
    border-radius: 50%;
    background: var(--bark);
  }
  .brand-name {
    margin: 0;
    color: var(--bark);
    font-weight: 400;
    font-size: 96px;
    line-height: 1.1;
    letter-spacing: 6px;
    text-align: center;
  }
  .divider {
    position: absolute;
    left: 0;
    top: 736px;
    width: 100%;
    height: 30px;
    background: var(--lime);
  }
  .contact {
    position: absolute;
    left: 0;
    top: 766px;
    width: 100%;
    height: 428px;
    background: var(--bark);
    color: var(--cream);
    text-align: center;
  }
  .agent-name {
    margin: 0;
    position: absolute;
    top: 68px;
    width: 100%;
    font-size: 104px;
    font-weight: 400;
    line-height: 1;
    letter-spacing: 16px;
  }
  .agent-phone {
    margin: 0;
    position: absolute;
    top: 176px;
    width: 100%;
    font-size: 118px;
    line-height: 1;
    letter-spacing: 2px;
  }
  .agent-web {
    margin: 0;
    position: absolute;
    top: 340px;
    width: 100%;
    font-size: 46px;
    line-height: 1;
  }
</style>
</head>
<body>
  <main class="sign">
    <header class="brand">
      <span class="brand-mark" aria-hidden="true"></span>
      <h1 class="brand-name">Maplewood<br>Home Tour</h1>
    </header>
    <div class="divider"></div>
    <section class="contact">
      <p class="agent-name">DANA REYES</p>
      <p class="agent-phone">626-555-0148</p>
      <p class="agent-web">www.findyourcaliforniahome.com</p>
    </section>
  </main>
</body>
</html>
```